Identity Package (Logo, Website)

We need a logo and website design for a new company.
The new company is a voicemail transcription service provider. It's name is KB7LUX.io
It will be very transactional. We like the "bootstrap" look and feel, and will be using a developer familiar with bootstrap. Here are the kinds of webpages we like :
https://www.plinverotrack.io
http://www.quorvix.com/
http://www.brenmoda.com/
There will only be 5 pages, as follows :
1- Homepage
2- Voicemail Transcription for Individuals
3- Voicemail Transcription for Companies
4- Wholesale Voicemail Transcription for Service Providers/Enterprises
5- Contact us
As far as the logo is concerned, we'd like to have just stylized text. It should be done in such a way as to make it easy to see the different elements of the name, which are KB, 7, and LUX.
Reason: I have received a number of designs, but the designs are mostly from the same few designers (not that much variety in designers). I'd like a few more to compare if possible, so I thought I would keep this open until Monday to give more designers the opportunity to submit over the weekend. Thanks!

```html
<!DOCTYPE html>
<html lang="en">
<head>
<meta charset="utf-8">
<title>KB7LUX.io – Voicemail Transcription</title>
<link rel="stylesheet" href="https://fonts.googleapis.com/css2?family=Open+Sans:wght@400;600;700&family=Exo+2:ital,wght@1,800&family=PT+Sans:wght@700&family=Arimo:wght@400;700&family=Roboto+Condensed:wght@300&display=swap">
<style>
:root{
  --navy:#275b7f;
  --navy-text:#2a5877;
  --sand:#f3dca8;
  --sand-deep:#e8cf95;
  --orange:#f6a21a;
  --yellow:#fdc70f;
  --mint:#7bc2a8;
  --mint-dark:#5fae92;
  --green-name:#5bb08a;
  --ink:#333333;
  --grey:#555555;
  --muted:#888888;
  --footer:#4b6274;
  --social:#c9d3db;
  --white:#ffffff;
}
*{margin:0;padding:0;box-sizing:border-box}
html,body{width:1200px;height:2748px;overflow:hidden}
body{position:relative;background:var(--white);font-family:"Open Sans",Arial,sans-serif;color:var(--ink)}
a{text-decoration:none;color:inherit}
.abs{position:absolute}

/* brand */
.brand{display:flex;align-items:center;gap:12px;color:var(--white);font-family:"Open Sans",sans-serif;font-weight:600;font-size:44px;line-height:1;white-space:nowrap}
.brand-dot{width:46px;height:46px;border-radius:50%;background:var(--white)}

/* header */
.site-header{left:0;top:0;width:1200px;height:92px;background:var(--navy)}
.header-brand{left:33px;top:22px}
.nav-link{top:40px;font-family:"Arimo",Arial,sans-serif;font-size:17px;line-height:22px;color:var(--white);white-space:nowrap}
.nav-login{left:1070px;top:34px;width:90px;height:34px;line-height:34px;text-align:center;background:var(--yellow);color:var(--navy);border-radius:9px;font-family:"Arimo",Arial,sans-serif;font-size:17px;white-space:nowrap}

/* hero */
.hero{left:0;top:92px;width:1200px;height:591px;background:var(--sand)}
.hero-title{left:29px;top:325px;font-family:"Exo 2",sans-serif;font-style:italic;font-weight:800;color:var(--navy);line-height:1;white-space:nowrap}
.hero-title .l1{display:block;font-size:52px}
.hero-title .l1 em{color:var(--orange);font-style:italic}
.hero-title .l2{display:block;font-size:33px;margin-top:10px}
.hero-copy{left:33px;top:433px;width:540px;font-size:20px;line-height:25px;color:#2b3a44}
.hero-art{left:632px;top:150px;width:513px;height:486px;border-radius:50%;background:radial-gradient(circle at 50% 50%,var(--sand-deep) 0%,var(--sand) 70%)}

/* intro */
.intro-title{left:0;top:782px;width:1200px;text-align:center;font-size:44px;font-weight:700;color:var(--navy-text);white-space:nowrap}
.intro-copy{left:185px;top:858px;width:830px;text-align:center;font-size:29px;line-height:36px;color:var(--grey)}

/* services */
.services{left:0;top:1066px;width:1200px;height:559px;background:var(--mint)}
.service{width:360px;color:var(--white)}
.service-card{position:relative;margin:0 auto;width:260px;height:154px;background:var(--white);border-radius:8px;display:flex;align-items:center;justify-content:center}
.service-card::after{content:"";position:absolute;left:118px;bottom:-12px;border-left:12px solid transparent;border-right:12px solid transparent;border-top:12px solid var(--white)}
.service-icon{width:96px;height:96px;border-radius:50%;background:var(--mint-dark)}
.service h3{margin-top:40px;text-align:center;font-size:24px;line-height:30px;font-weight:700}
.service p{margin:30px 0 0 40px;width:320px;font-size:17px;line-height:20px}

/* testimonials */
.reviews-title{left:0;top:1705px;width:1200px;text-align:center;font-family:"PT Sans",sans-serif;font-weight:700;font-size:44px;color:var(--ink)}
.avatar{width:123px;height:123px;border-radius:50%;background:linear-gradient(160deg,#efe6dc,#d9c2ae)}
.review{font-size:17px;line-height:20.5px;color:var(--ink);white-space:nowrap}
.review .name{display:block;margin-top:14px;font-family:"Arimo",sans-serif;font-weight:700;font-size:20px;color:var(--green-name)}
.review .role{display:block;margin-top:2px;font-family:"Arimo",sans-serif;font-size:14px;color:var(--muted)}

/* call to action */
.cta{left:0;top:2250px;width:1200px;height:220px;background:var(--yellow)}
.cta-text{left:0;top:2284px;width:1200px;text-align:center;color:var(--white);font-size:37px;white-space:nowrap}
.cta-button{left:458px;top:2356px;width:284px;height:81px;background:var(--white);display:flex;align-items:center;justify-content:center;gap:18px;color:var(--orange);font-weight:700;font-size:27px;white-space:nowrap}

/* footer */
.site-footer{left:0;top:2470px;width:1200px;height:278px;background:var(--footer)}
.footer-brand{left:33px;top:2540px;font-size:40px}
.footer-brand .brand-dot{width:42px;height:42px}
.copyright{left:33px;top:2600px;font-family:"Arimo",sans-serif;font-size:14px;color:var(--white);white-space:nowrap}
.footer-heading{top:2537px;font-family:"Open Sans",sans-serif;font-weight:700;font-size:24px;letter-spacing:-.3px;color:var(--white);white-space:nowrap}
.social{left:339px;top:2587px;display:flex;gap:14px}
.social span{width:55px;height:55px;border-radius:50%;background:var(--social)}
.foot-links{top:2582px;list-style:none;font-family:"Arimo",sans-serif;font-size:17px;line-height:19.6px;color:var(--white);white-space:nowrap}
.contact-lines{left:940px;top:2586px;font-family:"Arimo",sans-serif;font-size:17px;line-height:20px;color:var(--white);white-space:nowrap}
.phone{left:936px;top:2634px;display:flex;align-items:center;gap:8px;font-family:"Roboto Condensed",sans-serif;font-weight:300;font-size:34px;line-height:1;color:var(--white);white-space:nowrap}
</style>
</head>
<body>

<header class="site-header abs"></header>
<div class="brand header-brand abs"><span class="brand-dot"></span>kb7lux</div>
<a class="nav-link abs" href="#" style="left:623px">FEATURES</a>
<a class="nav-link abs" href="#" style="left:749px">PRICING</a>
<a class="nav-link abs" href="#" style="left:857px">LEARNING</a>
<a class="nav-link abs" href="#" style="left:982px">SIGN UP</a>
<a class="nav-login abs" href="#">LOGIN</a>

<section class="hero abs"></section>
<h1 class="hero-title abs"><span class="l1">YOUR <em>NO.1</em> VOICEMAIL</span><span class="l2">TRANSCRIPTION SERVICE PROVIDER</span></h1>
<p class="hero-copy abs">Duis autem vel eum iriure dolor in hendrerit in vulputate velit esse molestie consequat, vel illum dolore eu feugiat nulla facilisis at vero eros et accumsan et iusto odio.</p>
<div class="hero-art abs" role="img" aria-label="Illustration of a smartphone playing a voicemail, surrounded by phone, email and chat icons on a dashed orbit"></div>

<h2 class="intro-title abs">Lorem ipsum dolor sit amet consectetuer</h2>
<p class="intro-copy abs">Ut wisi enim ad minim veniam, quis nostrud exerci tation ullamcorper suscipit lobortis nisl ut aliquip ex ea commodo consequat.</p>

<section class="services abs"></section>
<div class="service abs" style="left:14px;top:1149px">
  <div class="service-card"><div class="service-icon" role="img" aria-label="Icon of a single person"></div></div>
  <h3>Voicemail Transcription<br>for Individuals</h3>
  <p>Typi non habent claritatem insitam est usus legentis in iis qui facit eorum claritatem. Investigationes demonstraverunt lectores legere me lius quod ii legunt saepius.</p>
</div>
<div class="service abs" style="left:419px;top:1149px">
  <div class="service-card"><div class="service-icon" role="img" aria-label="Icon of a group of people"></div></div>
  <h3>Voicemail Transcription<br>for Companies</h3>
  <p>Typi non habent claritatem insitam est usus legentis in iis qui facit eorum claritatem. Investigationes demonsrunt lectores legere me lius quod ii l.</p>
</div>
<div class="service abs" style="left:815px;top:1149px">
  <div class="service-card"><div class="service-icon" role="img" aria-label="Icon of people in front of a globe network"></div></div>
  <h3>Voicemail Transcription<br>for Service Providers /<br>Enterprises</h3>
  <p style="margin-top:26px">Typi non habent claritatem insitam est usus legentis in iis qui facit eorum claritatem. Investigationes demonstrnt lectores legere me lius quod ii legunt.</p>
</div>

<h2 class="reviews-title abs">What People Say About KB7LUX</h2>
<div class="avatar abs" style="left:122px;top:1857px" role="img" aria-label="Portrait photo of a customer"></div>
<div class="avatar abs" style="left:516px;top:1857px" role="img" aria-label="Portrait photo of a customer"></div>
<div class="avatar abs" style="left:925px;top:1857px" role="img" aria-label="Portrait photo of a customer"></div>

<div class="review abs" style="left:38px;top:2020px">Vel illum dolore eu feugiat nulla<br>facilisis at vero eros et accumsan et iusto<br>dignissim qui blandit praesent lupt<br>zril delenit augue duis dolore te feugait<br>nulla facilisi.<span class="name">Tomas Verhaegen</span><span class="role">Accounting Officer</span></div>
<div class="review abs" style="left:429px;top:2020px">Typi non habent claritatem insitam est us<br>legentis in iis qui facit eorum claritatem.<br>Investigationes demonstraverunt lectores<br>legere me lius quod ii legunt saepius.<span class="name">Marcus Ellory</span><span class="role">Accounting Officer</span></div>
<div class="review abs" style="left:832px;top:2020px">Claritas est etiam processus dynamicus<br>sequitur mutationem consuetudium<br>lectorum. Mirum est notare quam littera<br>gothica, quam nunc pumus parum clam,<br>anteposuerit litterarum formas.<span class="name">Noemi Castrell</span><span class="role">President, CEO of Dravelink</span></div>

<section class="cta abs"></section>
<p class="cta-text abs">Create your account today. No credit card required.</p>
<a class="cta-button abs" href="#">
  <svg width="40" height="40" viewBox="0 0 40 40" aria-hidden="true"><circle cx="20" cy="20" r="20" fill="#f6a21a"/><path d="M10 20h17M20 12l8 8-8 8" stroke="#fff" stroke-width="4" fill="none" stroke-linecap="round" stroke-linejoin="round"/></svg>
  GET STARTED
</a>

<footer class="site-footer abs"></footer>
<div class="brand footer-brand abs"><span class="brand-dot"></span>kb7lux</div>
<p class="copyright abs">© 2014 KB7LUX. All Rights Reserved.</p>

<h4 class="footer-heading abs" style="left:339px">CONNECT WITH US</h4>
<div class="social abs"><span></span><span></span><span></span></div>

<h4 class="footer-heading abs" style="left:630px">NAVIGATION</h4>
<ul class="foot-links abs" style="left:632px"><li>Home</li><li>About</li><li>Products</li><li>Services</li><li>Brands</li></ul>
<ul class="foot-links abs" style="left:746px"><li>Sitemap</li><li>Webshop</li><li>Terms of Use</li><li>Privacy Policy</li><li>Contact Us</li></ul>

<h4 class="footer-heading abs" style="left:940px">CONTACT US</h4>
<p class="contact-lines abs">#52 Harbor Lane, State, Country<br>email : info@kb7lux.io</p>
<p class="phone abs">
  <svg width="30" height="30" viewBox="0 0 32 32" aria-hidden="true"><circle cx="16" cy="16" r="14" fill="none" stroke="#fff" stroke-width="2"/><path d="M11 9c1-1 2-1 3 0l1.5 2.5c.5 1 0 1.7-.8 2.3-.6.4-.5 1 0 1.8 1 1.5 2 2.5 3.5 3.5.8.5 1.4.6 1.8 0 .6-.8 1.3-1.3 2.3-.8L25 20c1 1 1 2 0 3-2 2-5 1.5-8.5-2S9 13 11 9z" fill="#fff"/></svg>
  015.550.0142
</p>

</body>
</html>
```